Kivo Commercial Cleaning is lookong for a new business card design.

A fresh new design that's professional and stylish. We need a serious upgrade to our business cards. I have included pictures of our existing ones. Our clients include professional individuals and business owners. We woupdblike something professional and upbeat. Please have fun and see what you come uo with.

Target Market(s)

Property managers, business owners, facility managers and other similar professionals

Industry/Entity Type

Janitorial

Contact Information for Business Card

Name, cell, office number, email, web address

Font styles to use
Sans Serif

Colors

Designer to choose colors to be used in the design.

Requirements
Must have
• please use the green color in our logo
Nice to have
• Bar code
Should not have
• Address

```html
<!DOCTYPE html>
<html lang="en">
<head>
<meta charset="utf-8">
<title>Kivo Commercial Cleaning – Business Card</title>
<link href="https://fonts.googleapis.com/css2?family=Quicksand:wght@700&family=Arimo:wght@400&display=swap" rel="stylesheet">
<style>
  :root {
    --bg: #121212;
    --card: #2b2b2b;
    --card-back: #262626;
    --green: #2fb24a;
    --blue: #3a6fb5;
    --ink: #f2f2f2;
    --divider: #d8d8d8;
    --emboss: #333333;
  }
  * { box-sizing: border-box; margin: 0; padding: 0; }
  html, body {
    width: 1200px; height: 963px; overflow: hidden;
    background: var(--bg);
  }
  .canvas {
    position: relative; width: 1200px; height: 963px;
    display: flex; flex-direction: column; align-items: center; justify-content: center; gap: 44px;
  }
  .card {
    position: relative; width: 700px; height: 400px;
    border-radius: 26px;
    border: 3px solid var(--green);
    overflow: hidden;
  }
  .card--front { background: var(--card); }
  .card--back { background: var(--card-back); display: flex; align-items: center; justify-content: center; }

  .brand {
    position: absolute; left: 60px; top: 128px; width: 240px;
    font-family: "Quicksand", sans-serif; font-weight: 700;
    color: var(--green); line-height: 1.05;
  }
  .brand__name { font-size: 70px; letter-spacing: -1px; display: block; }
  .brand__line { font-size: 22px; display: block; margin-top: 6px; }

  .divider {
    position: absolute; left: 330px; top: 110px; width: 1.5px; height: 180px;
    background: var(--divider);
  }

  .contact { position: absolute; left: 362px; top: 126px; }
  .contact__name {
    font-family: "Quicksand", sans-serif; font-weight: 700;
    color: var(--green); font-size: 34px; line-height: 1; margin-bottom: 26px;
  }
  .contact__list { list-style: none; font-family: "Arimo", sans-serif; color: var(--ink); font-size: 19px; }
  .contact__item { display: flex; align-items: center; gap: 12px; margin-bottom: 11px; }
  .contact__icon { width: 18px; height: 18px; flex: none; }

  .back-name {
    font-family: "Quicksand", sans-serif; font-weight: 700;
    font-size: 150px; color: var(--emboss); letter-spacing: -3px;
  }
</style>
</head>
<body>
<main class="canvas">
  <section class="card card--front" aria-label="Business card front">
    <div class="brand">
      <span class="brand__name">kivo</span>
      <span class="brand__line">commercial cleaning</span>
    </div>
    <div class="divider"></div>
    <div class="contact">
      <h1 class="contact__name">dana whitfield</h1>
      <ul class="contact__list">
        <li class="contact__item">
          <svg class="contact__icon" viewBox="0 0 24 24" fill="none" stroke="#2fb24a" stroke-width="2" stroke-linecap="round" stroke-linejoin="round"><path d="M6 3h3l2 5-2.5 1.5a11 11 0 0 0 6 6L16 13l5 2v3a2 2 0 0 1-2 2A16 16 0 0 1 4 5a2 2 0 0 1 2-2z"/><path d="M15 3a6 6 0 0 1 6 6"/><path d="M15 7a2 2 0 0 1 2 2"/></svg>
          (555) 014-2870
        </li>
        <li class="contact__item">
          <svg class="contact__icon" viewBox="0 0 24 24" fill="none" stroke="#2fb24a" stroke-width="2" stroke-linejoin="round"><rect x="3" y="5" width="18" height="14" rx="1"/><path d="M3 6l9 7 9-7"/></svg>
          dana@kivocleaning.com
        </li>
        <li class="contact__item">
          <svg class="contact__icon" viewBox="0 0 24 24" fill="none" stroke="#2fb24a" stroke-width="2"><circle cx="12" cy="12" r="9"/><path d="M3 12h18M12 3a14 14 0 0 1 0 18M12 3a14 14 0 0 0 0 18"/></svg>
          www.kivocleaning.com
        </li>
      </ul>
    </div>
  </section>

  <section class="card card--back" aria-label="Business card back">
    <span class="back-name">kivo</span>
  </section>
</main>
</body>
</html>
```